High-end residential home builder needs a business card design

We need a new business card design for a small residential construction company based in Boise, Idaho. We specialize in building custom high-end homes and remodels, with a focus on great design and craftsmanship.

We would like to use our current logo, but open to new color suggestions.
Just looking for a clean, sharp, modern design that looks high-end.

Target Market(s)

Upscale clientele

Industry/Entity Type

Contractor

Contact Information for Business Card

Company: Stonefield Custom Builders
Name: Marcus Tilley
Phone number: 208 367 4120
Email: MarcusTilleySCB@mailbox-example.com
Website: Stonefieldcustombuilders-example.com

Font styles to use
Serif
Sans Serif

Requirements
Must have
• Company Logo
Company name
My name
My phone number
My email
Company website
Nice to have
• I have attached a few photos of cards that I really like.

```html
<!DOCTYPE html>
<html lang="en">
<head>
<meta charset="utf-8">
<title>Stonefield Custom Builders — Business Card</title>
<link href="https://fonts.googleapis.com/css2?family=Arimo:wght@400;700&display=swap" rel="stylesheet">
<style>
  :root {
    --backdrop: #141414;
    --card: #202020;
    --ink: #f2f2f2;
    --ink-soft: #d4d4d4;
    --emboss: #3a3a3a;
    --rule: #bdbdbd;
  }
  * { margin: 0; padding: 0; box-sizing: border-box; }
  html, body {
    width: 1200px; height: 901px; overflow: hidden;
    background: var(--backdrop);
    font-family: "Arimo", Arial, sans-serif;
  }
  .sheet {
    width: 1200px; height: 901px;
    display: flex; flex-direction: column; align-items: center; justify-content: center;
    gap: 40px;
  }
  .card {
    width: 700px; height: 400px;
    background: var(--card);
    position: relative;
    box-shadow: 0 10px 30px rgba(0,0,0,.5);
  }
  /* back side */
  .card-back { display: flex; align-items: center; justify-content: center; }
  .card-back .wordmark {
    color: var(--emboss);
    font-size: 30px; font-weight: 700;
    letter-spacing: 4px; text-transform: uppercase; text-align: center; line-height: 1.35;
  }
  /* front side */
  .card-front { display: flex; align-items: center; }
  .brand {
    width: 330px; display: flex; flex-direction: column; align-items: center; gap: 14px;
  }
  .brand .mark-square { width: 22px; height: 22px; background: var(--ink); }
  .brand .wordmark {
    color: var(--ink); font-size: 16px; font-weight: 400;
    letter-spacing: 3px; text-transform: uppercase; text-align: center; line-height: 1.6;
  }
  .divider { width: 1px; height: 160px; background: var(--rule); }
  .contact { padding-left: 34px; color: var(--ink); }
  .contact .person { font-size: 34px; font-weight: 700; letter-spacing: -0.5px; }
  .contact .role { font-size: 18px; color: var(--ink-soft); margin-top: 4px; margin-bottom: 22px; }
  .contact ul { list-style: none; }
  .contact li {
    display: flex; align-items: center; gap: 9px;
    font-size: 16px; line-height: 1.75; color: var(--ink-soft);
  }
  .contact svg { width: 14px; height: 14px; flex: none; fill: none; stroke: var(--ink); stroke-width: 1.6; }
</style>
</head>
<body>
<main class="sheet">
  <section class="card card-back" aria-label="Card back">
    <div class="wordmark">Stonefield<br>Custom Builders</div>
  </section>

  <section class="card card-front" aria-label="Card front">
    <div class="brand">
      <span class="mark-square"></span>
      <div class="wordmark">Stonefield<br>Custom Builders</div>
    </div>
    <span class="divider"></span>
    <div class="contact">
      <div class="person">Marcus Tilley</div>
      <div class="role">Founder &amp; CEO</div>
      <ul>
        <li>
          <svg viewBox="0 0 16 16" aria-hidden="true"><path d="M4 1.5l2.5 3-1.5 2a8 8 0 0 0 4.5 4.5l2-1.5 3 2.5-1.5 2.5C7 14 2 9 1.5 3z"/></svg>
          208 367 4120
        </li>
        <li>
          <svg viewBox="0 0 16 16" aria-hidden="true"><rect x="1.5" y="3.5" width="13" height="9"/><path d="M1.5 3.5l6.5 5.5 6.5-5.5"/></svg>
          MarcusTilleySCB@mailbox-example.com
        </li>
        <li>
          <svg viewBox="0 0 16 16" aria-hidden="true"><circle cx="8" cy="8" r="6.5"/><ellipse cx="8" cy="8" rx="3" ry="6.5"/><path d="M1.5 8h13"/></svg>
          Stonefieldcustombuilders-example.com
        </li>
      </ul>
    </div>
  </section>
</main>
</body>
</html>
```